Home Services Website Design and Revisions

We have started to create a website but I would like to get some ideas and a quote on how to create a more professional website then what we have created thus far.

http://brinkhavenhomecare.example/

Pages I would need on the site

Home page - company summary and brand promise
who we are
what we do - services offered
our promise to quality and client experience
client experiences - testimonials and pictures
Promotions
Career opportunities - Join The team
Updates

Target Market(s)

Homeowners in the DFW region

Industry/Entity Type

Home Improvement

Number of Pages Required

5+ page

Font styles to use
Sans Serif

Requirements
Must have
• Home page - company summary and brand promise
• who we are
• what we do - services offered
• our promise to quality and client experience
• client experiences - testimonials and pictures
• Promotions
• Career opportunities - Join The team
• logo
• pictures
• links to social media sites
• A very impactful home page
• With a image of home and family.
• a beautiful home, yard and pictures of a loving family smiling and enjoying their home.
Nice to have
• Pictures with people to create emotion
• we don't work on houses
• we work on homes with families that trust us to provide quality services in a timely manner
• Families that trust us as their partner when they need work at their home with their family
Should not have
• low quality images or images just of homes

```html
<!DOCTYPE html>
<html lang="en">
<head>
<meta charset="utf-8">
<title>Career Opportunities – Brinkhaven Home Care</title>
<link href="https://fonts.googleapis.com/css2?family=Open+Sans:wght@400;600&family=Raleway:wght@400;500&display=swap" rel="stylesheet">
<style>
:root{
  --green:#62bb0e;
  --text:#333;
  --muted:#666;
  --field:#f4f4f4;
  --grey-btn:#aaaaaa;
  --footer-bg:#f7f7f7;
  --white:#fff;
}
*{box-sizing:border-box;margin:0;padding:0}
html,body{width:1200px;height:871px;overflow:hidden;background:var(--white);font-family:"Open Sans",sans-serif;color:var(--text)}
.page{position:relative;width:1200px;height:871px}
.abs{position:absolute}

.site-header{left:0;top:0;width:1200px;height:47px}
.brand{left:89px;top:12px;display:flex;align-items:center;gap:8px;font-size:17px;font-weight:600;color:var(--text)}
.brand-mark{width:20px;height:20px;background:var(--green)}
.main-nav{right:90px;top:0;display:flex;gap:21px;font-size:12.5px;height:47px;align-items:center}
.main-nav a{color:var(--text);text-decoration:none;position:relative;height:47px;line-height:52px}
.main-nav a.active{color:var(--green)}
.main-nav a.active::after{content:"";position:absolute;left:-2px;right:-2px;bottom:0;height:2px;background:var(--green)}

.page-banner{left:0;top:47px;width:1200px;height:68px;background:var(--green);color:var(--white)}
.page-banner h1{position:absolute;left:88px;top:21px;font-family:"Raleway",sans-serif;font-weight:400;font-size:21px}
.breadcrumb{position:absolute;right:89px;top:27px;font-size:12px}

.cv-title{left:88px;top:139px;font-family:"Raleway",sans-serif;font-weight:400;font-size:21px;color:#444}
.field{background:var(--field);font-size:12px;color:#555;padding:0 13px;display:flex;align-items:center;height:37px}
.field.tall{align-items:flex-start;padding-top:13px}
.field.placeholder{color:#999;font-size:13px}
.btn{display:flex;align-items:center;justify-content:center;color:var(--white);font-size:12px;border-radius:2px}
.btn.grey{background:var(--grey-btn)}
.btn.green{background:var(--green)}

.site-footer{left:0;top:651px;width:1200px;height:186px;background:var(--footer-bg)}
.footer-col h3{font-family:"Raleway",sans-serif;font-weight:500;font-size:16px;color:#222;margin-bottom:13px}
.footer-col p,.footer-col li{font-size:12px;color:var(--muted);line-height:19.5px;list-style:none}
.footer-col li{line-height:22.3px}
.socials{display:flex;gap:6px;margin-top:14px}
.socials span{width:32px;height:32px;border-radius:50%}
.contact-row{display:flex;align-items:center;gap:9px;font-size:12px;color:var(--text);margin-bottom:12px}
.contact-icon{width:28px;height:28px;background:var(--green);display:flex;align-items:center;justify-content:center}
.news-input{width:230px;height:37px;border:1px solid #ddd;background:var(--white);font-size:12px;color:#555;display:flex;align-items:center;padding-left:12px;margin-left:1px}
.news-btn{width:114px;height:36px;margin:9px 0 0 1px;font-size:12px}

.to-top{left:1068px;top:812px;width:48px;height:48px;border-radius:50%;background:var(--white);border:1px solid #e2e2e2;display:flex;align-items:center;justify-content:center;z-index:2}
.copyright{left:0;top:837px;width:1200px;height:34px;background:var(--green);color:var(--white);font-size:12px;padding:9px 0 0 90px}
</style>
</head>
<body>
<div class="page">
  <header class="site-header abs">
    <div class="brand abs"><span class="brand-mark"></span>Brinkhaven Home Care</div>
    <nav class="main-nav abs">
      <a class="active" href="#">Home</a>
      <a href="#">Who we are</a>
      <a href="#">What we do</a>
      <a href="#">Client experiences</a>
      <a href="#">Career Opportunities</a>
    </nav>
  </header>

  <section class="page-banner abs">
    <h1>Career Opportunities</h1>
    <div class="breadcrumb">Home / Career Opportunities</div>
  </section>

  <h2 class="cv-title abs">Drop your CV</h2>
  <div class="field abs" style="left:89px;top:180px;width:336px">First Name</div>
  <div class="field abs" style="left:431px;top:180px;width:336px">Last Name</div>
  <div class="field abs" style="left:775px;top:180px;width:336px">Email</div>
  <div class="field abs" style="left:89px;top:224px;width:507px;padding-left:16px">Phone no</div>
  <div class="field abs" style="left:603px;top:224px;width:507px">Phone no</div>
  <div class="field tall abs" style="left:89px;top:268px;width:1021px;height:288px;padding-left:17px">Message</div>
  <div class="field placeholder abs" style="left:89px;top:572px;width:350px">Upload Resume</div>
  <div class="btn grey abs" style="left:447px;top:573px;width:93px;height:32px">Browse Doc</div>
  <div class="btn grey abs" style="left:548px;top:572px;width:96px;height:34px">Upload Doc</div>
  <div class="btn green abs" style="left:652px;top:572px;width:96px;height:34px">Submit</div>

  <footer class="site-footer abs">
    <div class="footer-col abs" style="left:89px;top:15px;width:240px">
      <h3>About Us</h3>
      <p>Lorem Ipsum is simply dummy text of the printing and typesetting industry. Lorem Ipsum has been the industry's</p>
      <div class="socials">
        <span style="background:#3b5998"></span>
        <span style="background:#2fc2ef"></span>
        <span style="background:#dd3526"></span>
        <span style="background:#1c4a7a"></span>
      </div>
    </div>
    <div class="footer-col abs" style="left:397px;top:15px">
      <h3>Useful Links</h3>
      <ul>
        <li>Site Map</li><li>Email</li><li>Privacy Policy</li><li>Terms of Service</li><li>Delivery and Returns</li>
      </ul>
    </div>
    <div class="footer-col abs" style="left:597px;top:15px">
      <h3>Get In Touch</h3>
      <div class="contact-row">
        <span class="contact-icon"><svg width="12" height="12" viewBox="0 0 24 24"><path fill="#fff" d="M6.6 10.8a15 15 0 006.6 6.6l2.2-2.2c.3-.3.7-.4 1-.2 1.1.4 2.3.6 3.6.6.6 0 1 .4 1 1V20c0 .6-.4 1-1 1A17 17 0 013 4c0-.6.4-1 1-1h3.5c.6 0 1 .4 1 1 0 1.3.2 2.5.6 3.6.1.3 0 .7-.2 1z"/></svg></span>
        123 -456-7890
      </div>
      <div class="contact-row">
        <span class="contact-icon"><svg width="13" height="10" viewBox="0 0 26 20"><path fill="#fff" d="M0 0h26v20H0z"/><path fill="none" stroke="#62bb0e" stroke-width="2" d="M1 1l12 10L25 1M1 19l9-9M25 19l-9-9"/></svg></span>
        info@domain.com
      </div>
    </div>
    <div class="footer-col abs" style="left:871px;top:15px">
      <h3>Newsletter</h3>
      <div class="news-input">Email</div>
      <div class="btn green news-btn">SEND</div>
    </div>
  </footer>

  <div class="to-top abs"><svg width="12" height="8" viewBox="0 0 12 8"><path d="M1 7l5-5 5 5" fill="none" stroke="#62bb0e" stroke-width="1.6"/></svg></div>
  <div class="copyright abs">Copyright 2016 | All Right Reserved</div>
</div>
</body>
</html>
```